Moms Beyond Gnats

My company name is Moms beyond gnats. We do residential and commercial mosquito control. See attached brochure and logo.

Target Market(s)

My target market is upper middle class families in the midwestern part of the US.

Requirements
Must have
• Form to collect customer information

```html
<!DOCTYPE html>
<html lang="en">
<head>
<meta charset="utf-8">
<title>Moms Beyond Gnats</title>
<link rel="stylesheet" href="https://fonts.googleapis.com/css2?family=Arimo:ital,wght@0,400;0,700;1,700&display=swap">
<style>
  :root {
    --yellow: #ffe11a;
    --yellow-deep: #f7c800;
    --ink: #222222;
    --text: #333333;
    --green: #4b9e38;
    --green-dark: #13703a;
    --green-light: #2f9a4c;
    --footer: #121212;
    --white: #ffffff;
    --line: #cfcfcf;
    --field: #eef0f2;
  }
  * { box-sizing: border-box; margin: 0; padding: 0; }
  html, body { width: 1149px; height: 1200px; overflow: hidden; background: var(--white); }
  body { font-family: "Arimo", Arial, sans-serif; color: var(--text); }
  .page {
    position: relative; width: 1024px; height: 1069px;
    transform: scale(1.1221); transform-origin: 0 0;
    background: linear-gradient(#f1f1f1 395px, #ffffff 560px);
  }
  .hero {
    position: absolute; left: 0; top: 0; width: 1024px; height: 396px;
    background: linear-gradient(180deg, #7ea6c6 0%, #c9b98a 45%, #d9b45a 62%, #6d7a34 78%, #4d5a26 100%);
  }
  .topline { position: absolute; left: 0; top: 0; width: 1024px; height: 8px; background: #1b1b1b; }
  .navbar {
    position: absolute; left: 31px; top: 8px; width: 961px; height: 42px;
    background: linear-gradient(var(--yellow), var(--yellow-deep));
    border-radius: 0 0 8px 8px; box-shadow: 0 2px 4px rgba(0,0,0,.3);
  }
  .nav { position: absolute; left: 230px; top: 14px; display: flex; gap: 32px; list-style: none; }
  .nav li { font-weight: 700; font-size: 16px; color: var(--ink); letter-spacing: .2px; }
  .call { position: absolute; right: 10px; top: 8px; font-size: 24px; font-weight: 700; color: #111; }
  .call em { font-size: 19px; font-weight: 400; font-style: italic; }
  .brand {
    position: absolute; left: 58px; top: 8px; width: 182px; height: 110px;
    background: var(--white); border-radius: 0 0 10px 10px; box-shadow: 0 3px 6px rgba(0,0,0,.35);
    display: flex; align-items: center; justify-content: center; text-align: center;
    font-size: 22px; font-weight: 700; color: var(--green-dark); line-height: 1.1;
  }
  .headline {
    position: absolute; left: 52px; top: 178px; width: 460px; text-align: center;
    font-size: 36px; font-weight: 700; font-style: italic; line-height: 42px; color: #3a3a3a;
    text-shadow: 1px 1px 0 #fff, -1px -1px 0 rgba(255,255,255,.6);
  }
  .headline .light { color: var(--white); text-shadow: 1px 2px 2px rgba(0,0,0,.5); }
  .about {
    position: absolute; left: 31px; top: 372px; width: 683px; height: 304px;
    background: var(--white); border-radius: 6px 6px 0 0; box-shadow: 0 4px 8px rgba(0,0,0,.12);
  }
  .tab {
    position: absolute; left: 20px; top: 402px; width: 338px; height: 39px;
    background: linear-gradient(var(--yellow), var(--yellow-deep)); border-radius: 0 8px 8px 0;
    font-size: 19px; color: #111; padding: 9px 0 0 23px;
  }
  .tab-fold { position: absolute; left: 20px; top: 441px; }
  .thumb { position: absolute; left: 45px; top: 458px; width: 122px; height: 80px;
    background: linear-gradient(135deg, #4f6b2e, #a7b37a 55%, #5b6e3a); }
  .copy { font-size: 13px; line-height: 17px; text-align: justify; color: #333; }
  .copy-left { position: absolute; left: 45px; top: 456px; width: 314px; }
  .copy-left .float { float: left; width: 131px; height: 82px; }
  .divider { position: absolute; left: 377px; top: 450px; width: 1px; height: 200px; background: var(--line); }
  .copy-right { position: absolute; left: 397px; top: 456px; width: 304px; }
  .where-title { position: absolute; left: 31px; top: 712px; font-size: 15px; font-weight: 700; color: var(--green); }
  .where-text { position: absolute; left: 31px; top: 740px; width: 392px; font-size: 16px; line-height: 19.5px; color: #333; }
  .cafe { position: absolute; left: 430px; top: 713px; width: 284px; height: 114px; border: 1px solid #bbb;
    background: linear-gradient(120deg, #8a7a4e, #d7c7a4 40%, #f0e9da 60%, #7d8b5a); }
  .form-card {
    position: absolute; left: 733px; top: 328px; width: 259px; height: 457px;
    background: var(--white); border-radius: 8px; box-shadow: 0 0 4px rgba(0,0,0,.3);
  }
  .form-head {
    height: 67px; border-radius: 8px 8px 0 0; color: var(--white); text-align: center;
    font-size: 20px; font-weight: 700; line-height: 26px; padding-top: 7px;
    background: linear-gradient(var(--green-light), var(--green-dark));
  }
  .form-body { padding: 24px 13px 0 13px; }
  .form-body label { display: block; font-size: 12px; font-weight: 700; color: #333; margin-bottom: 9px; }
  .field { display: block; width: 230px; height: 32px; background: var(--field); padding: 3px; margin-bottom: 18px; }
  .field span { display: block; height: 100%; background: var(--white); border: 1px solid #c3c8cc; border-radius: 3px; }
  .field.tall { height: 110px; margin-bottom: 10px; }
  .submit {
    display: block; margin-left: auto; margin-right: 7px; width: 81px; height: 31px;
    background: linear-gradient(#ffe86a, #f4c000); border: 1px solid #d9ae00; border-radius: 3px;
    font-family: "Arimo", Arial, sans-serif; font-size: 13px; color: #333;
  }
  .footer { position: absolute; left: 0; top: 883px; width: 1024px; height: 186px; background: var(--footer); color: var(--white); }
  .footer h4 { position: absolute; left: 31px; top: 15px; font-size: 12px; font-weight: 700; }
  .footer address { position: absolute; left: 31px; top: 44px; font-style: normal; font-size: 12px; line-height: 14px; }
  .footer-links { position: absolute; right: 32px; top: 15px; font-size: 12px; list-style: none; display: flex; }
  .footer-links li + li::before { content: "|"; margin: 0 6px; }
  .footer-rule { position: absolute; left: 22px; top: 140px; width: 980px; height: 1px; background: #262626; }
  .copyright { position: absolute; right: 31px; top: 147px; font-size: 11px; }
</style>
</head>
<body>
<div class="page">
  <div class="hero" role="img" aria-label="Family walking hand in hand on a sunny lakeside meadow"></div>
  <div class="topline"></div>
  <header class="navbar">
    <ul class="nav"><li>HOME</li><li>ABOUT US</li><li>OUR SERVICES</li><li>CONTACT US</li></ul>
    <div class="call"><em>Call</em> 555.214.7300</div>
  </header>
  <div class="brand">Moms Beyond<br>Gnats</div>
  <h1 class="headline">Rid your outside areas of pesky and dangerous bugs <span class="light">the safe way!</span></h1>

  <section class="about"></section>
  <div class="tab">Why Moms Beyond Gnats?</div>
  <svg class="tab-fold" width="12" height="8"><path d="M0 0H12V8Z" fill="#111"/></svg>
  <div class="thumb" role="img" aria-label="Child playing outdoors on the grass"></div>
  <p class="copy copy-left"><span class="float"></span>Moms Beyond Gnats is the only scheduled spraying service devoted exclusively to protecting your outdoor area against mosquitoes and other pests all season long! M.B.G! also offers an all natural "bee friendly" bee deterrent which is ideal for outdoor eating areas which attract pesky bees. Just call 555-214-7300 to schedule an evaluation appointment. Once applied, M.B.G! is a long acting product that reamins effective for weeks.</p>
  <div class="divider"></div>
  <p class="copy copy-right">Not only do you want to keep your customers and employes happy, but safety is also an issue. West Nile Virus is a real threat, with Illinois ranking as one of the states with the most confirmed human cases. Not only will M.B.G! protect your business against West Nile, it also eliminates or reduces the dangers of Encephalitis and allergic reactions caused by insect bites.</p>

  <h2 class="where-title">Where Can Moms Beyond Gnats Be Sprayed?</h2>
  <p class="where-text">Anywhere outside. M.B.G! offers excellent service for public pools, outdoor cafes and beer gardens, baseball fields, courtyards, public places such as fountains or town squares, and office gathering areas.</p>
  <div class="cafe" role="img" aria-label="Guests enjoying a salad lunch at an outdoor cafe"></div>

  <form class="form-card">
    <div class="form-head">Schedule an Evaluation<br>Appointment</div>
    <div class="form-body">
      <label>Name</label><span class="field"><span></span></span>
      <label>Phone Number</label><span class="field"><span></span></span>
      <label>Email</label><span class="field"><span></span></span>
      <label>Address</label><span class="field tall"><span></span></span>
      <button class="submit" type="button">SUBMIT</button>
    </div>
  </form>

  <footer class="footer">
    <h4>MOMS BEYOND GNATS</h4>
    <address>Address 1<br>Address 2<br><br>Phone: 555 214 7300<br>Fax: 555 214 7301</address>
    <ul class="footer-links"><li>Home</li><li>About Us</li><li>Our Services</li><li>Contact Us</li><li>Privacy</li><li>Terms &amp; Conditions</li></ul>
    <div class="footer-rule"></div>
    <p class="copyright">Copyright © 2010 Moms Beyond Gnats, All Rights Reserved</p>
  </footer>
</div>
</body>
</html>
```